Modern Innovative Business Card Design

We require a nice, modern, clean business card design, ready for upload to Cardomora. Our company develops online banking software solutions for small financial insitutions. The design should be clean, professional, but yet not "corporate boring". See www.fyrolt.com for an idea of business image and profile. The design should communicate innovation, be modern and fresh, yet look professional and established.

Target Market(s)

Finance industry, bankers, entrepreneurs

Industry/Entity Type

Financial

Contact Information for Business Card

Tobias Wendlerup
CEO

FYROLT BV
Lindenwerf 38
1027 HX Amsterdam
The Netherlands

Phone: +31 20 517 8036
Direct: +31 20 604 1758
Skype: tobias.fyrolt
ceo@fyrolt.com
www.fyrolt.com

Font styles to use
Sans Serif

Requirements
Must have
• Should look clean, modern and professional. File should be ready for upload to cardomora.
Should not have
• Boring standard corporate layout

```html
<!DOCTYPE html>
<html lang="en">
<head>
<meta charset="utf-8">
<title>FYROLT business card</title>
<link href="https://fonts.googleapis.com/css2?family=Arimo:wght@400;700&display=swap" rel="stylesheet">
<style>
  :root {
    --page: #e9e7e3;
    --card-dark: #161616;
    --card-light: #e6e6e6;
    --accent: #8cc21e;
    --ink-light: #ffffff;
    --logo-silver: #b4b4b4;
    --logo-dark: #3b3b3b;
  }
  * { margin: 0; padding: 0; box-sizing: border-box; }
  html, body {
    width: 1200px; height: 1200px; overflow: hidden;
    background: var(--page);
    font-family: "Arimo", Arial, sans-serif;
  }
  .canvas { position: relative; width: 1200px; height: 1200px; }
  .card {
    position: absolute; left: 180px; width: 840px; height: 480px;
    overflow: hidden; box-shadow: 0 6px 18px rgba(0,0,0,.18);
  }
  .card--front { top: 80px; background: var(--card-dark); }
  .card--back { top: 640px; background: var(--card-light); }

  .wordmark {
    position: absolute; font-weight: 700; letter-spacing: 6px;
    font-size: 64px; line-height: 1;
  }
  .card--front .wordmark {
    color: var(--logo-silver); left: 0; right: 0; top: 170px; text-align: center;
  }
  .card--back .wordmark {
    color: var(--logo-dark); left: 470px; top: 208px;
  }

  .rule { position: absolute; height: 4px; background: var(--accent); top: 370px; }
  .rule--left { left: 0; width: 300px; }
  .rule--right { right: 0; width: 300px; }
  .front-url {
    position: absolute; left: 300px; width: 240px; top: 361px;
    text-align: center; color: var(--ink-light); font-size: 18px; letter-spacing: 1px;
  }

  .split { position: absolute; inset: 0; }
  .identity { position: absolute; left: 50px; top: 52px; }
  .identity__name { color: var(--accent); font-size: 27px; letter-spacing: 1px; }
  .identity__title { color: var(--ink-light); font-size: 17px; margin-top: 2px; }

  .contacts { position: absolute; left: 50px; top: 190px; list-style: none; }
  .contacts li {
    display: flex; align-items: flex-start; gap: 10px;
    color: var(--ink-light); font-size: 17px; line-height: 26px;
  }
  .contacts svg { width: 16px; height: 16px; margin-top: 5px; flex: none; }
</style>
</head>
<body>
<main class="canvas">

  <section class="card card--front" aria-label="Card front">
    <div class="wordmark">FYROLT</div>
    <div class="rule rule--left"></div>
    <div class="front-url">WWW.FYROLT.COM</div>
    <div class="rule rule--right"></div>
  </section>

  <section class="card card--back" aria-label="Card back">
    <svg class="split" viewBox="0 0 840 480" aria-hidden="true">
      <polygon points="0,0 450,0 320,480 0,480" fill="var(--card-dark)"/>
    </svg>

    <div class="identity">
      <div class="identity__name">TOBIAS WENDLERUP</div>
      <div class="identity__title">CEO FYROLT BV</div>
    </div>

    <ul class="contacts">
      <li>
        <svg viewBox="0 0 16 16"><path fill="var(--accent)" d="M4 1l3 3-2 2c1 2 3 4 5 5l2-2 3 3-2 3C7 15 1 9 1 3z"/></svg>
        +31 20 604 1758
      </li>
      <li>
        <svg viewBox="0 0 16 16"><path fill="var(--accent)" d="M4 1l3 3-2 2c1 2 3 4 5 5l2-2 3 3-2 3C7 15 1 9 1 3z"/></svg>
        +31 20 517 8036
      </li>
      <li>
        <svg viewBox="0 0 16 16"><circle cx="8" cy="8" r="7" fill="var(--accent)"/></svg>
        tobias.fyrolt
      </li>
      <li>
        <svg viewBox="0 0 16 16"><rect x="1" y="3" width="14" height="10" fill="var(--accent)"/><path d="M1 3l7 6 7-6" fill="none" stroke="var(--card-dark)" stroke-width="1.4"/></svg>
        ceo@fyrolt.com
      </li>
      <li>
        <svg viewBox="0 0 16 16"><circle cx="8" cy="8" r="7" fill="var(--accent)"/><path d="M1 8h14M8 1c-3 3-3 11 0 14M8 1c3 3 3 11 0 14" fill="none" stroke="var(--card-dark)" stroke-width="1.2"/></svg>
        www.fyrolt.com
      </li>
      <li>
        <svg viewBox="0 0 16 16"><path fill="var(--accent)" d="M8 0a6 6 0 0 0-6 6c0 4 6 10 6 10s6-6 6-10a6 6 0 0 0-6-6z"/><circle cx="8" cy="6" r="2.3" fill="var(--card-dark)"/></svg>
        <span>Lindenwerf 38 1027 HX Amsterdam<br>The Netherlands</span>
      </li>
    </ul>

    <div class="wordmark">FYROLT</div>
  </section>

</main>
</body>
</html>
```